"Haven" Women's Bible Class promotional poster

We need a poster that we can also transform into a postcard and possibly isolate the word HAVEN in order to use as logo for other items. I will attach the poster used previously. Would like something much better. I do like the lightbulb idea and think it might be interesting to have several bulbs with only one shining brightly. This is geared mainly for young women so do want something that would appeal to them. Other ideas welcome. I've seen tree growing in lite bulb that's neat, but could also incorporate any of your own ideas. Open to what will draw their attention. Want more color than the example given from last year. This was not interesting enough. Even lightbulb combined with simple floral. We want to stress the word 'HAVEN'
Haven Women's Ministry; Arise, shine' for your light has come, And the glory of the Lord has risen upon you. Isaiah 60:1; Sunday AM Bible Class; …through it all...busy schedules, careers, families, babies…;

```html
<!DOCTYPE html>
<html lang="en">
<head>
<meta charset="utf-8">
<title>Haven Women's Ministry Poster</title>
<link href="https://fonts.googleapis.com/css2?family=Montserrat:wght@400&family=Source+Sans+3:wght@300;400;600&display=swap" rel="stylesheet">
<style>
  :root {
    --page-bg: #ffffff;
    --poster-top: #2f3e5c;
    --poster-bottom: #5a3d63;
    --glow: #f6c453;
    --glow-soft: rgba(246, 196, 83, 0.35);
    --ink-white: #ffffff;
    --ink-verse: #fbe7b5;
    --ink-muted: #f2b4a8;
    --ink-accent: #f6c453;
    --ink-ghost: rgba(255, 255, 255, 0.16);
  }
  html, body {
    margin: 0;
    padding: 0;
    width: 1200px;
    height: 3514px;
    overflow: hidden;
    background: var(--page-bg);
  }
  .poster {
    position: absolute;
    left: 33px;
    top: 33px;
    width: 1134px;
    height: 1487px;
    background: linear-gradient(180deg, var(--poster-top) 0%, var(--poster-bottom) 100%);
    overflow: hidden;
    font-family: "Source Sans 3", "Myriad Pro", sans-serif;
    text-align: center;
  }
  .poster > * {
    position: absolute;
    left: 0;
    width: 100%;
    margin: 0;
  }
  .brand-mark {
    left: 537px;
    width: 60px;
    height: 60px;
    top: 168px;
    border-radius: 50%;
    background: var(--glow);
    box-shadow: 0 0 40px 18px var(--glow-soft);
  }
  .brand-name {
    top: 250px;
    font-family: "Montserrat", sans-serif;
    font-weight: 400;
    font-size: 160px;
    line-height: 180px;
    letter-spacing: 0;
    color: var(--ink-white);
  }
  .brand-tagline {
    top: 420px;
    display: flex;
    justify-content: center;
    align-items: center;
    gap: 14px;
    font-family: "Montserrat", sans-serif;
    font-size: 23px;
    line-height: 30px;
    letter-spacing: 5px;
    color: var(--ink-accent);
  }
  .brand-tagline .rule {
    width: 96px;
    height: 2px;
    background: var(--ink-accent);
  }
  .verse {
    top: 540px;
    font-size: 31px;
    line-height: 42px;
    color: var(--ink-verse);
  }
  .verse-ref {
    top: 634px;
    font-size: 29px;
    line-height: 40px;
    font-weight: 600;
    color: var(--ink-white);
  }
  .life-line {
    top: 758px;
    font-size: 31px;
    line-height: 43px;
    color: var(--ink-verse);
  }
  .audience {
    top: 924px;
    font-size: 31px;
    line-height: 43px;
    color: var(--ink-verse);
  }
  .provisions {
    top: 1090px;
    font-size: 29px;
    line-height: 40px;
    font-weight: 300;
    text-transform: uppercase;
    color: var(--ink-muted);
  }
  .venue {
    top: 1206px;
    font-size: 30px;
    line-height: 43px;
    font-weight: 600;
    text-transform: uppercase;
    color: var(--ink-white);
  }
  .ghost-name {
    left: 585px;
    width: auto;
    top: 1345px;
    font-family: "Montserrat", sans-serif;
    font-weight: 400;
    font-size: 190px;
    line-height: 220px;
    color: var(--ink-ghost);
    white-space: nowrap;
    text-align: left;
  }
</style>
</head>
<body>
  <main class="poster">
    <span class="brand-mark" aria-hidden="true"></span>
    <h1 class="brand-name">HAVEN</h1>
    <div class="brand-tagline">
      <span class="rule"></span>
      <span>WOMEN'S MINISTRY</span>
      <span class="rule"></span>
    </div>
    <p class="verse">Arise, shine; for your light has come,<br>And the glory of the Lord has risen upon you.</p>
    <p class="verse-ref">Isaiah 60:1</p>
    <p class="life-line">…through it all...busy schedules,<br>careers, families, babies…</p>
    <p class="audience">Bible Study geared just for<br>Women Ages 20 - 40</p>
    <p class="provisions">Dinner, childcare &amp; children's classes provided</p>
    <p class="venue">Maplewood Chapel<br>Sunday AM Bible Class</p>
    <div class="ghost-name" aria-hidden="true">HAVEN</div>
  </main>
</body>
</html>
```